Design a powerpoint background using company logo/colours

We require a powerpoint background that incorporates our company colours and logo. I have attached the logo in various sizes.

Have fun and be imaginative

Our company colours are white and Red-236, Green-22 and Blue 86.
Please use these colours in designing the ppt background

Industry/Entity Type

It Company

Colors

Designer to choose colors to be used in the design.

```html
<!DOCTYPE html>
<html lang="en">
<head>
<meta charset="utf-8">
<title>Nexaro – Slide Background</title>
<link href="https://fonts.googleapis.com/css2?family=Tulpen+One&family=Open+Sans:ital,wght@1,400&display=swap" rel="stylesheet">
<style>
  :root {
    --brand-red: #ec1656;
    --white: #ffffff;
    --tagline-grey: #6b6b6b;
  }
  * { margin: 0; padding: 0; box-sizing: border-box; }
  html, body { width: 1200px; height: 900px; overflow: hidden; }
  body { background: var(--brand-red); }

  .slide {
    position: relative;
    width: 1200px;
    height: 900px;
    overflow: hidden;
    background: var(--brand-red);
  }

  .hero-visual {
    position: absolute;
    left: 640px;
    top: 300px;
    width: 560px;
    height: 600px;
    background:
      radial-gradient(ellipse at 45% 65%, rgba(200, 8, 60, 0.5) 0%, rgba(230, 30, 90, 0.3) 40%, rgba(236, 22, 86, 0) 72%),
      radial-gradient(ellipse at 70% 30%, rgba(255, 120, 160, 0.22) 0%, rgba(236, 22, 86, 0) 60%);
  }

  .corner-badge {
    position: absolute;
    left: 0;
    top: 0;
    width: 400px;
    height: 230px;
  }

  .brand {
    position: absolute;
    left: 36px;
    top: 26px;
    display: flex;
    flex-direction: column;
  }
  .brand-row { display: flex; align-items: center; gap: 14px; }
  .brand-name {
    font-family: "Tulpen One", sans-serif;
    font-size: 84px;
    line-height: 1;
    color: var(--brand-red);
    letter-spacing: 2px;
  }
  .brand-dot {
    width: 26px;
    height: 26px;
    background: var(--brand-red);
  }
  .brand-tagline {
    font-family: "Open Sans", sans-serif;
    font-style: italic;
    font-size: 15px;
    color: var(--tagline-grey);
    margin-top: 4px;
  }

  .rule {
    position: absolute;
    height: 2px;
    background: var(--white);
  }
  .rule-top { left: 360px; top: 137px; width: 802px; }
  .rule-bottom { left: 142px; top: 812px; width: 1020px; }

  .slide-title {
    position: absolute;
    left: 158px;
    top: 378px;
    font-family: "Tulpen One", sans-serif;
    font-weight: 400;
    font-size: 176px;
    line-height: 1;
    letter-spacing: 8px;
    color: var(--white);
    white-space: nowrap;
    transform: scaleX(1.42);
    transform-origin: left top;
  }
</style>
</head>
<body>
  <main class="slide">
    <div class="hero-visual" role="img" aria-label="Faded photograph of a telecommunications tower"></div>

    <svg class="corner-badge" viewBox="0 0 400 230" aria-hidden="true">
      <ellipse cx="60" cy="-60" rx="320" ry="275" fill="var(--white)"/>
    </svg>

    <header class="brand">
      <div class="brand-row">
        <span class="brand-name">nexaro</span>
        <span class="brand-dot"></span>
      </div>
      <span class="brand-tagline">Linking your business now</span>
    </header>

    <div class="rule rule-top"></div>
    <div class="rule rule-bottom"></div>

    <h1 class="slide-title">1024x768:96dpi</h1>
  </main>
</body>
</html>
```